Brochure Front Page Design Project

We need concepts for the front page of a clients brochure (A4 Portrait)
The client is a power products distributor (Lawnmowers, Trimmers, Blowers etc) and are looking for a clean fresh brochure.

No restrictions, any colours, full use of images, line art or renderings - lets see what we can generate.

Best concept wins!
Updates

The clients have advised they would like to see some concepts with an aesthetic similar to the following linkĀ http://www.varnholt.com/au/products/trimmers-brushcutters/

Industry/Entity Type

Distributor

Requirements
Must have
• Must incorporate their logo

Product Images (More images available from their site http://www.quillborough.com.au/)
Nice to have
• The clients have advised they would like to see some concepts utilizing Black simple designs as well - similar to http://www.varnholt.com/au/products/trimmers-brushcutters/

```html
<!DOCTYPE html>
<html lang="en">
<head>
<meta charset="utf-8">
<title>Brelton Australia – Brochure Front Page</title>
<link rel="stylesheet" href="https://fonts.googleapis.com/css2?family=Open+Sans:wght@400;600;700&display=swap">
<style>
  :root {
    --stage: #d9d4cc;
    --paper: #ffffff;
    --ink: #1c1c1c;
    --ink-soft: #333333;
    --band-black: #1f1f1f;
    --brand-green: #4cb35a;
    --footer-grey: #ececec;
    --rule-grey: #c8c8c8;
    --lawn-dark: #2e3a22;
    --lawn-mid: #58702f;
    --lawn-light: #7d9448;
  }
  * { box-sizing: border-box; margin: 0; padding: 0; }
  html, body {
    width: 869px; height: 1200px; overflow: hidden;
    background: var(--stage);
    font-family: "Open Sans", Arial, sans-serif;
    color: var(--ink);
  }
  .flyer {
    position: absolute; left: 35px; top: 35px;
    width: 798px; height: 1128px;
    background: linear-gradient(to bottom, var(--paper) 0, var(--paper) 760px, #e9e9e9 1027px);
    overflow: hidden;
    box-shadow: 0 2px 8px rgba(0,0,0,.25);
  }
  .hero { position: absolute; left: 0; top: 0; width: 798px; height: 560px; }
  .intro {
    position: absolute; left: 19px; top: 416px; width: 420px;
    font-size: 16.4px; line-height: 22.8px; color: var(--ink-soft);
  }
  .product {
    position: absolute; top: 570px; width: 243px;
  }
  .product--mower-black { left: 19px; }
  .product--trimmer { left: 276px; }
  .product--mower-red { left: 534px; }
  .product__photo {
    width: 243px; height: 192px; border-radius: 12px;
    box-shadow: 0 2px 6px rgba(0,0,0,.35);
  }
  .product__photo--mower-black { background: linear-gradient(to bottom, #4f6a3a 0, #2b2b2b 40%, #7f8286 70%, #5d8a3a 100%); }
  .product__photo--trimmer { background: linear-gradient(135deg, #3f6a2e 0, #5b8fc9 30%, #b32a2a 55%, #4f7a32 100%); }
  .product__photo--mower-red { background: linear-gradient(to bottom, #5a7a3c 0, #c8292b 30%, #8a8d92 65%, #4f8236 100%); }
  .product__text {
    margin: 14px 8px 0 8px;
    font-size: 10.6px; line-height: 14.5px; text-align: justify; color: var(--ink-soft);
  }
  .product__features { list-style: none; margin: 5px 8px 0 8px; }
  .product__features li {
    font-size: 10.6px; line-height: 17.1px; color: var(--ink-soft);
    padding-left: 12px; position: relative;
  }
  .product__features li::before { content: "•"; position: absolute; left: 0; }
  .divider {
    position: absolute; top: 775px; width: 1px; height: 252px;
    background: linear-gradient(to bottom, rgba(150,150,150,0), #9a9a9a 40%, #bdbdbd);
  }
  .divider--one { left: 270px; }
  .divider--two { left: 525px; }
  .contact-bar {
    position: absolute; left: 0; top: 1027px; width: 798px; height: 101px;
    background: var(--footer-grey); border-top: 1px solid var(--rule-grey);
  }
  .brand {
    position: absolute; left: 22px; top: 30px;
    display: flex; align-items: center; gap: 10px;
  }
  .brand__mark { width: 22px; height: 22px; background: var(--brand-green); }
  .brand__name { font-size: 34px; font-weight: 700; color: var(--ink); letter-spacing: 1px; }
  .contact {
    position: absolute; left: 254px; top: 8px;
    font-size: 16.2px; line-height: 23px; color: var(--ink);
  }
  .contact strong { font-weight: 700; font-size: 17px; }
  .contact .sep { color: #555; margin: 0 3px; }
</style>
</head>
<body>
  <main class="flyer">
    <svg class="hero" viewBox="0 0 798 560" aria-hidden="false">
      <defs>
        <linearGradient id="lawnScene" x1="0" y1="0" x2="0" y2="1">
          <stop offset="0" stop-color="#1f2a18"/>
          <stop offset="0.45" stop-color="var(--lawn-dark)"/>
          <stop offset="0.6" stop-color="var(--lawn-mid)"/>
          <stop offset="1" stop-color="var(--lawn-light)"/>
        </linearGradient>
      </defs>
      <rect x="0" y="0" width="798" height="430" fill="url(#lawnScene)" role="img" aria-label="Photo of a gardener trimming the edge of a lawn beside hedges"/>
      <path d="M0,350 C250,335 550,352 798,398 L798,485 C600,425 300,372 0,360 Z" fill="var(--band-black)"/>
      <path d="M0,360 C300,372 600,425 798,485 L798,560 L0,560 Z" fill="var(--paper)"/>
      <path d="M250,380 C480,392 680,440 798,485 L798,527 C650,455 450,398 250,380 Z" fill="var(--brand-green)"/>
    </svg>

    <p class="intro">Brelton Australia is an Australian owned and operated company. We have over 14 years experience in the outdoor power equipment industry in Australia. Our objective is to offer our dealers and customers quality products at the best possible prices, with excellent back up of spare parts and service.</p>

    <section class="product product--mower-black">
      <div class="product__photo product__photo--mower-black" role="img" aria-label="Photo of a black-engine push mower on grass"></div>
      <p class="product__text">Lorem Ipsum is simply dummy text of the printing and typesetting industry. Lorem Ipsum has been the industry's standard dummy text ever since the 1500s, when an unknown printer took a galley of type and scrambled it to make a type specimen book.</p>
      <ul class="product__features">
        <li>Lorem Ipsum is simply dummy</li><li>Lorem Ipsum is simply dummy</li><li>Lorem Ipsum is simply dummy</li><li>Lorem Ipsum is simply dummy</li><li>Lorem Ipsum is simply dummy</li><li>Lorem Ipsum is simply dummy</li><li>Lorem Ipsum is simply dummy</li><li>Lorem Ipsum is simply dummy</li>
      </ul>
    </section>

    <section class="product product--trimmer">
      <div class="product__photo product__photo--trimmer" role="img" aria-label="Photo of a red line trimmer held over a lawn"></div>
      <p class="product__text">Lorem Ipsum is simply dummy text of the printing and typesetting industry. Lorem Ipsum has been the industry's standard dummy text ever since the 1500s, when an unknown printer took a galley of type and scrambled it to make a type specimen book.</p>
      <ul class="product__features">
        <li>Lorem Ipsum is simply dummy</li><li>Lorem Ipsum is simply dummy</li><li>Lorem Ipsum is simply dummy</li><li>Lorem Ipsum is simply dummy</li><li>Lorem Ipsum is simply dummy</li><li>Lorem Ipsum is simply dummy</li><li>Lorem Ipsum is simply dummy</li><li>Lorem Ipsum is simply dummy</li>
      </ul>
    </section>

    <section class="product product--mower-red">
      <div class="product__photo product__photo--mower-red" role="img" aria-label="Photo of a red-engine push mower on grass"></div>
      <p class="product__text">Lorem Ipsum is simply dummy text of the printing and typesetting industry. Lorem Ipsum has been the industry's standard dummy text ever since the 1500s, when an unknown printer took a galley of type and scrambled it to make a type specimen book.</p>
      <ul class="product__features">
        <li>Lorem Ipsum is simply dummy</li><li>Lorem Ipsum is simply dummy</li><li>Lorem Ipsum is simply dummy</li><li>Lorem Ipsum is simply dummy</li><li>Lorem Ipsum is simply dummy</li><li>Lorem Ipsum is simply dummy</li><li>Lorem Ipsum is simply dummy</li><li>Lorem Ipsum is simply dummy</li>
      </ul>
    </section>

    <div class="divider divider--one"></div>
    <div class="divider divider--two"></div>

    <footer class="contact-bar">
      <div class="brand">
        <span class="brand__mark"></span>
        <span class="brand__name">BRELTON</span>
      </div>
      <div class="contact">
        <p>Contact Us : <strong>+1 234 567 80</strong><span class="sep">|</span>Email Us : <strong>email@breltonaustralia.com.au</strong></p>
        <p>Log On : www.breltonaustralia.com.au</p>
        <p>Suite #123, Street Name, Area Name, State Name, Country Code.</p>
      </div>
    </footer>
  </main>
</body>
</html>
```